Label for kLw Homestead beef tallow

I need a small label to go on a 2oz amber glass jar as well as a 4 oz. amber glass jar of moisturizer.
I prefer it to be rectangular for the 2oz jar since it's small and square for the 4oz jar.
I'd like to keep our kLw Homestead logo the same font and style, which is attached. Ten Sleep, Wyoming should be left out. The font for kLw Homestead is spartan.
The label content is as follows:
Signature Tallow
Whipped Moisturizer
Ingredients: Beef Tallow, jojoba oil, peppermint oil.
2oz. jar

Instead of a white label, I'm thinking of a tan or brown label that will blend in with the amber jar. The lettering could then be a white, cream or even rust/burgandy color. Something to give it a rich look.

Thank you!

Target Market(s)

Mainly women but men as well.

Industry/Entity Type

Ranching and online beef sales

Requirements
Must have
• kLw Homestead logo

```html
<!DOCTYPE html>
<html lang="en">
<head>
<meta charset="utf-8">
<title>kLw Homestead – Signature Tallow Labels</title>
<link rel="stylesheet" href="https://fonts.googleapis.com/css2?family=League+Spartan:wght@400;700&display=swap">
<style>
  :root {
    --backdrop: #d3b48c;
    --label-brown: #654a40;
    --label-brown-deep: #5a4139;
    --cream: #d9b98f;
    --font-main: "League Spartan", "Futura", sans-serif;
  }
  * { box-sizing: border-box; margin: 0; padding: 0; }
  html, body {
    width: 1200px;
    height: 750px;
    overflow: hidden;
    background: var(--backdrop);
    font-family: var(--font-main);
  }
  .canvas {
    position: relative;
    width: 1200px;
    height: 750px;
  }
  .label {
    position: absolute;
    background: linear-gradient(90deg, var(--label-brown) 0%, var(--label-brown) 70%, var(--label-brown-deep) 100%);
    color: var(--cream);
  }
  .label::before,
  .label::after {
    content: "";
    position: absolute;
    left: 0;
    right: 0;
    height: 8px;
    background: var(--cream);
  }
  .label::before { top: 0; }
  .label::after { bottom: 0; }

  .label--small {
    left: 80px;
    top: 230px;
    width: 480px;
    height: 300px;
  }
  .label--large {
    left: 650px;
    top: 150px;
    width: 450px;
    height: 450px;
  }

  .emblem {
    position: absolute;
    left: 50%;
    transform: translateX(-50%);
  }
  .label--small .emblem { top: 26px; width: 252px; height: 252px; }
  .label--large .emblem { top: 38px; width: 318px; height: 318px; }

  .emblem__arc {
    font-family: var(--font-main);
    font-weight: 700;
    font-size: 22px;
    letter-spacing: 2px;
    fill: var(--cream);
  }
  .emblem__name {
    font-family: var(--font-main);
    font-weight: 400;
    fill: var(--cream);
    text-anchor: middle;
  }
  .emblem__name--main { font-size: 56px; }
  .emblem__name--sub { font-size: 21px; letter-spacing: 2px; }

  .ingredients {
    position: absolute;
    font-weight: 700;
    font-size: 13px;
    line-height: 1.05;
    text-transform: uppercase;
    letter-spacing: 0.2px;
  }
  .label--small .ingredients {
    left: 16px;
    bottom: 28px;
    transform-origin: left bottom;
    transform: rotate(-90deg) translate(0, 100%);
    white-space: nowrap;
  }
  .label--large .ingredients {
    left: 34px;
    bottom: 32px;
    font-size: 15px;
  }

  .net-weight {
    position: absolute;
    font-weight: 700;
    font-size: 17px;
    letter-spacing: 0.5px;
  }
  .label--small .net-weight { right: 12px; bottom: 28px; }
  .label--large .net-weight { right: 34px; bottom: 44px; font-size: 18px; }
</style>
</head>
<body>
<main class="canvas">

  <section class="label label--small" aria-label="2 ounce jar label">
    <svg class="emblem" viewBox="0 0 300 300" aria-label="Signature Tallow, kLw Homestead, Whipped Moisturizer">
      <defs>
        <path id="arc-top-small" d="M 38,150 A 112,112 0 0 1 262,150"/>
        <path id="arc-bottom-small" d="M 16,150 A 134,134 0 0 0 284,150"/>
      </defs>
      <text class="emblem__arc"><textPath href="#arc-top-small" startOffset="50%" text-anchor="middle">SIGNATURE TALLOW</textPath></text>
      <text class="emblem__arc"><textPath href="#arc-bottom-small" startOffset="50%" text-anchor="middle">WHIPPED MOISTURIZER</textPath></text>
      <text class="emblem__name emblem__name--main" x="150" y="168">kLw</text>
      <text class="emblem__name emblem__name--sub" x="150" y="200">HOMESTEAD</text>
    </svg>
    <p class="ingredients">Beef Tallow, Jojoba Oil<br>Peppermint Oil.</p>
    <p class="net-weight">2OZ.</p>
  </section>

  <section class="label label--large" aria-label="4 ounce jar label">
    <svg class="emblem" viewBox="0 0 300 300" aria-label="Signature Tallow, kLw Homestead, Whipped Moisturizer">
      <defs>
        <path id="arc-top-large" d="M 38,150 A 112,112 0 0 1 262,150"/>
        <path id="arc-bottom-large" d="M 16,150 A 134,134 0 0 0 284,150"/>
      </defs>
      <text class="emblem__arc"><textPath href="#arc-top-large" startOffset="50%" text-anchor="middle">SIGNATURE TALLOW</textPath></text>
      <text class="emblem__arc"><textPath href="#arc-bottom-large" startOffset="50%" text-anchor="middle">WHIPPED MOISTURIZER</textPath></text>
      <text class="emblem__name emblem__name--main" x="150" y="168">kLw</text>
      <text class="emblem__name emblem__name--sub" x="150" y="200">HOMESTEAD</text>
    </svg>
    <p class="ingredients">Beef Tallow, Jojoba Oil<br>Peppermint Oil.</p>
    <p class="net-weight">4OZ.</p>
  </section>

</main>
</body>
</html>
```